KTV Lanternfall

I need a graphic package design for our new bodybuilding sports supplement. The artwork should be clean and useable for many formats. examples or great usage are www.ferrovigorlab.example, www.quartzpulse.example and http://www.belwinnutrition.example/ as examples. I am adding our logo for your reference. The name Lanternfall is because it will help make "Big Guns" as a catch phrase, the product line will have other supplements such as creatine and protein powders and the artwork should be useable on all products. You can see our website for ideas at www.kestovalife.example
Updates

Hi everyone, There are some nice entries coming in. I do wonder if some of you are reading the brief as a few labels don't even highlight the product, KTV is the company, Lanternfall is the Product. Thanks Tam

Industry/Entity Type

Supplement

```html
<!DOCTYPE html>
<html lang="en">
<head>
<meta charset="utf-8">
<title>KTV Lanternfall – Chewable Label Range</title>
<link href="https://fonts.googleapis.com/css2?family=Russo+One&family=Oswald:wght@500;600&family=Special+Elite&display=swap" rel="stylesheet">
<style>
  :root {
    --stage: #1a1a1a;
    --label-bg: #0b0b0c;
    --label-edge: #2a2a2c;
    --white: #f4f4f4;
    --soft: #cfcfcf;
    --band-light: #d9d9d9;
    --band-dark: #6b6b6b;
    --band-text: #ffffff;
    --rule: #7fae2e;
    --orange: #e27d22;
    --blue: #3d9fd9;
    --rose: #d79a8c;
    --lime: #a6d633;
    --red: #d8262b;
    --silver: #bfc3c7;
  }
  * { box-sizing: border-box; margin: 0; padding: 0; }
  html, body { width: 1200px; height: 756px; overflow: hidden; }
  body {
    background: var(--stage);
    display: flex;
    align-items: center;
    justify-content: center;
    gap: 56px;
  }
  .label {
    --accent: var(--orange);
    --name: var(--white);
    width: 240px;
    height: 640px;
    background: var(--label-bg);
    border: 1px solid var(--label-edge);
    border-radius: 6px;
    display: flex;
    flex-direction: column;
    align-items: center;
    padding-top: 34px;
    position: relative;
    overflow: hidden;
  }
  .label--blue { --accent: var(--blue); }
  .label--rose { --accent: var(--rose); }
  .label--lime { --accent: var(--lime); --name: var(--red); }
  .label--rose .claim-band { background: linear-gradient(180deg, #efe6d4, #9c927d 55%, #d8cfbc); }

  .brand {
    font-family: "Russo One", sans-serif;
    font-size: 40px;
    color: var(--white);
    letter-spacing: 1px;
    line-height: 1;
  }
  .hero {
    position: relative;
    width: 100%;
    height: 190px;
    margin-top: 14px;
  }
  .hero-art {
    position: absolute;
    inset: 0;
    background:
      radial-gradient(ellipse 40% 55% at 50% 55%, var(--accent), transparent 70%),
      radial-gradient(ellipse 70% 35% at 50% 45%, color-mix(in srgb, var(--accent) 45%, transparent), transparent 75%);
    opacity: .85;
  }
  .product-name {
    position: absolute;
    left: 0; right: 0; top: 52px;
    text-align: center;
    font-family: "Russo One", sans-serif;
    font-size: 30px;
    color: var(--name);
    letter-spacing: .5px;
  }
  .tagline {
    position: absolute;
    right: 22px; top: 96px;
    text-align: right;
    font-family: "Oswald", sans-serif;
    font-weight: 600;
    font-size: 13px;
    line-height: 1;
    text-transform: uppercase;
    color: var(--accent);
  }
  .tagline span { display: block; color: var(--white); font-size: 15px; }
  .claim-band {
    width: 100%;
    padding: 6px 0 7px;
    background: linear-gradient(180deg, var(--band-light), var(--band-dark) 55%, #a9a9a9);
    text-align: center;
    font-family: "Oswald", sans-serif;
    font-weight: 600;
    font-size: 20px;
    line-height: 1.1;
    color: var(--band-text);
    text-transform: uppercase;
    text-shadow: 0 1px 2px rgba(0,0,0,.5);
  }
  .benefits-title {
    margin-top: 16px;
    text-align: center;
    font-family: "Oswald", sans-serif;
    font-weight: 500;
    font-size: 14px;
    line-height: 1.2;
    color: var(--white);
    text-transform: uppercase;
  }
  .benefits {
    list-style: none;
    margin-top: 10px;
    width: 196px;
    font-family: "Special Elite", monospace;
    font-size: 10px;
    line-height: 1.25;
    color: var(--soft);
    text-transform: uppercase;
  }
  .benefits li { position: relative; padding-left: 11px; margin-bottom: 3px; }
  .benefits li::before {
    content: "";
    position: absolute; left: 0; top: 3px;
    width: 6px; height: 6px;
    border-radius: 50%;
    background: var(--accent);
  }
  .rule {
    margin-top: auto;
    width: 200px;
    height: 1px;
    background: var(--rule);
  }
  .count {
    margin: 8px 0 26px;
    font-family: "Special Elite", monospace;
    font-size: 12px;
    color: var(--white);
    letter-spacing: 1px;
  }
</style>
</head>
<body>

  <article class="label label--orange">
    <div class="brand">KTV</div>
    <div class="hero">
      <div class="hero-art" role="img" aria-label="Orange metallic blade shards radiating behind the product name"></div>
      <div class="product-name">LANTERNFALL</div>
      <div class="tagline">New<span>Chewable</span></div>
    </div>
    <div class="claim-band">Bigger Stronger<br>Muscles</div>
    <p class="benefits-title">Lanternfall's 3 Licensed and<br>Patented Ingredients Help</p>
    <ul class="benefits">
      <li>Increase Protein Synthesis while Reducing Protein Breakdown</li>
      <li>Increased Muscle Mass, Strength and Endurance</li>
      <li>Reduce Muscle Fatigue and Increase Blood Flow</li>
      <li>Increase Joint Range of Motion &amp; Decrease Joint Discomfort</li>
    </ul>
    <div class="rule"></div>
    <p class="count">100 chewable tablet</p>
  </article>

  <article class="label label--blue">
    <div class="brand">KTV</div>
    <div class="hero">
      <div class="hero-art" role="img" aria-label="Blue metallic blade shards radiating behind the product name"></div>
      <div class="product-name">LANTERNFALL</div>
      <div class="tagline">New<span>Chewable</span></div>
    </div>
    <div class="claim-band">Bigger Stronger<br>Muscles</div>
    <p class="benefits-title">Lanternfall's 3 Licensed and<br>Patented Ingredients Help</p>
    <ul class="benefits">
      <li>Increase Protein Synthesis while Reducing Protein Breakdown</li>
      <li>Increased Muscle Mass, Strength and Endurance</li>
      <li>Reduce Muscle Fatigue and Increase Blood Flow</li>
      <li>Increase Joint Range of Motion &amp; Decrease Joint Discomfort</li>
    </ul>
    <div class="rule"></div>
    <p class="count">100 chewable tablet</p>
  </article>

  <article class="label label--rose">
    <div class="brand">KTV</div>
    <div class="hero">
      <div class="hero-art" role="img" aria-label="Rose-gold metallic blade shards radiating behind the product name"></div>
      <div class="product-name">LANTERNFALL</div>
      <div class="tagline">New<span>Chewable</span></div>
    </div>
    <div class="claim-band">Bigger Stronger<br>Muscles</div>
    <p class="benefits-title">Lanternfall's 3 Licensed &amp;<br>Patented Ingredients Help:</p>
    <ul class="benefits">
      <li>Increase Protein Synthesis while Reducing Protein Breakdown</li>
      <li>Increased Muscle Mass, Strength and Endurance</li>
      <li>Reduce Muscle Fatigue and Increase Blood Flow</li>
      <li>Increase Joint Range of Motion &amp; Decrease Joint Discomfort</li>
    </ul>
    <div class="rule"></div>
    <p class="count">100 chewable tablet</p>
  </article>

  <article class="label label--lime">
    <div class="brand">KTV</div>
    <div class="hero">
      <div class="hero-art" role="img" aria-label="Silver metallic blade shards with a lime glow behind the product name"></div>
      <div class="product-name">LANTERNFALL</div>
      <div class="tagline">New<span>Chewable</span></div>
    </div>
    <div class="claim-band">Bigger Stronger<br>Muscles</div>
    <p class="benefits-title">Lanternfall's 3 Licensed and<br>Patented Ingredients Help</p>
    <ul class="benefits">
      <li>Increase Protein Synthesis while Reducing Protein Breakdown</li>
      <li>Increased Muscle Mass, Strength and Endurance</li>
      <li>Reduce Muscle Fatigue and Increase Blood Flow</li>
      <li>Increase Joint Range of Motion &amp; Decrease Joint Discomfort</li>
    </ul>
    <div class="rule"></div>
    <p class="count">100 chewable tablet</p>
  </article>

</body>
</html>
```